Bakery Business Cards

We are in need of business cards for our bakery business--something non-generic that reflects our business and will stand out. We are a wholesale bakery that primarily services in-store bakeries, casinos, schools, distributors, and fund-raising companies. The family business was founded in 1960. (www.marlowsovenworks.com)

```html
<!DOCTYPE html>
<html lang="en">
<head>
<meta charset="utf-8">
<title>Marlow's Ovenworks Business Cards</title>
<link href="https://fonts.googleapis.com/css2?family=Montserrat:wght@400;500;700;800&display=swap" rel="stylesheet">
<style>
  :root {
    --brand-blue: #2a52a6;
    --brand-blue-deep: #1f4596;
    --card-white: #ffffff;
    --card-shade: #eceef1;
    --ink: #2b2b2b;
    --backdrop: #2e2e2e;
    --pastry-light: #e6c08a;
    --pastry-dark: #b2553e;
  }
  * { box-sizing: border-box; margin: 0; padding: 0; }
  html, body { width: 1200px; height: 900px; overflow: hidden; }
  body {
    background: var(--backdrop);
    font-family: "Montserrat", sans-serif;
    position: relative;
  }
  .card {
    position: absolute;
    top: 118px;
    width: 380px;
    height: 665px;
    border-radius: 28px;
    overflow: hidden;
  }
  .card--front {
    left: 170px;
    background: linear-gradient(160deg, var(--card-shade), var(--card-white) 60%);
    color: var(--brand-blue);
    text-align: center;
  }
  .card--back {
    left: 650px;
    background: linear-gradient(180deg, var(--brand-blue-deep), var(--brand-blue));
    color: var(--card-white);
  }
  .brand {
    position: absolute;
    left: 0; right: 0;
    top: 90px;
    text-align: center;
  }
  .brand__name {
    font-weight: 800;
    font-size: 36px;
    line-height: 1.1;
    letter-spacing: 0.5px;
  }
  .brand__since {
    margin-top: 10px;
    font-weight: 700;
    font-size: 15px;
    letter-spacing: 3px;
    text-transform: uppercase;
  }
  .person { position: absolute; top: 300px; left: 0; right: 0; }
  .person__name { font-weight: 800; font-size: 24px; }
  .person__role { font-size: 14px; color: var(--ink); margin-top: 4px; }
  .divider {
    position: absolute; left: 40px; right: 40px;
    display: flex; align-items: center; gap: 12px;
  }
  .divider::before, .divider::after {
    content: ""; flex: 1; height: 2px; background: var(--brand-blue);
  }
  .divider--contact { top: 378px; }
  .divider--address { top: 520px; }
  .icon-chip {
    width: 30px; height: 30px; border-radius: 6px;
    background: var(--brand-blue);
    display: flex; align-items: center; justify-content: center;
  }
  .icon-chip svg { width: 18px; height: 18px; }
  .contact-list {
    position: absolute; top: 428px; left: 0; right: 0;
    list-style: none; font-size: 14px; color: var(--ink); line-height: 26px;
  }
  .address {
    position: absolute; top: 572px; left: 0; right: 0;
    font-size: 14px; color: var(--ink); line-height: 20px;
  }
  .gallery {
    position: absolute; left: 24px; right: 24px; top: 330px;
    display: grid; grid-template-columns: repeat(3, 1fr); gap: 12px;
  }
  .gallery__tile {
    height: 104px; border-radius: 16px;
    background: radial-gradient(circle at 50% 55%, var(--pastry-light), #f4ede4 70%);
  }
  .gallery__feature {
    position: absolute; left: 24px; right: 24px; top: 460px; height: 180px;
    border-radius: 18px;
    background: linear-gradient(135deg, var(--pastry-light), var(--pastry-dark) 55%, var(--pastry-light));
  }
</style>
</head>
<body>

<section class="card card--front" aria-label="Card front">
  <div class="brand">
    <div class="brand__name">Marlow's<br>Ovenworks</div>
    <div class="brand__since">Since 1960</div>
  </div>

  <div class="person">
    <div class="person__name">Daniel Marlow</div>
    <div class="person__role">Managing Director</div>
  </div>

  <div class="divider divider--contact">
    <span class="icon-chip"><svg viewBox="0 0 24 24" fill="#fff"><path d="M6.6 10.8a15 15 0 0 0 6.6 6.6l2.2-2.2a1 1 0 0 1 1-.25 11.4 11.4 0 0 0 3.6.57 1 1 0 0 1 1 1V20a1 1 0 0 1-1 1A17 17 0 0 1 3 4a1 1 0 0 1 1-1h3.5a1 1 0 0 1 1 1c0 1.25.2 2.45.57 3.57a1 1 0 0 1-.25 1z"/></svg></span>
    <span class="icon-chip"><svg viewBox="0 0 24 24" fill="#fff"><path d="M3 6h18v12H3z" opacity=".0"/><path d="M3 5h18a1 1 0 0 1 1 1v12a1 1 0 0 1-1 1H3a1 1 0 0 1-1-1V6a1 1 0 0 1 1-1zm1 2v.4l8 5 8-5V7z"/></svg></span>
    <span class="icon-chip"><svg viewBox="0 0 24 24" fill="none" stroke="#fff" stroke-width="2"><circle cx="12" cy="12" r="9"/><path d="M3 12h18M12 3c3 3.5 3 14.5 0 18M12 3c-3 3.5-3 14.5 0 18"/></svg></span>
  </div>

  <ul class="contact-list">
    <li>916-555-0148</li>
    <li>info@marlowsovenworks.com</li>
    <li>www.marlowsovenworks.com</li>
  </ul>

  <div class="divider divider--address">
    <span class="icon-chip"><svg viewBox="0 0 24 24" fill="#fff"><path d="M12 2a7 7 0 0 0-7 7c0 5 7 13 7 13s7-8 7-13a7 7 0 0 0-7-7zm0 9.5A2.5 2.5 0 1 1 12 6.5a2.5 2.5 0 0 1 0 5z"/></svg></span>
  </div>

  <p class="address">Here is your full address<br>Road no.123, Texas, USA</p>
</section>

<section class="card card--back" aria-label="Card back">
  <div class="brand">
    <div class="brand__name">Marlow's<br>Ovenworks</div>
    <div class="brand__since">Since 1960</div>
  </div>

  <div class="gallery">
    <div class="gallery__tile" role="img" aria-label="Slice of berry pie on a plate"></div>
    <div class="gallery__tile" role="img" aria-label="Slice of peach pie on a plate"></div>
    <div class="gallery__tile" role="img" aria-label="Slice of peach pie with a fork"></div>
  </div>
  <div class="gallery__feature" role="img" aria-label="Whole lattice-top cherry pie among baked pies"></div>
</section>

</body>
</html>
```